Food Menu Design for Japanese Restaurant

Design a food menu for a high-end Japanese food restaurant. See attached detailed requirements file and menu items.

Industry/Entity Type

Restaurant

Colors

Designer to choose colors to be used in the design.

Requirements
Must have
• All menu items, descriptions, prices, add-ons, as provided in requirements file, all shown on designed menu and formatted.

```html
<!DOCTYPE html>
<html lang="en">
<head>
<meta charset="UTF-8">
<title>Mizuro — Starters &amp; Soup</title>
<link rel="stylesheet" href="https://fonts.googleapis.com/css2?family=Pathway+Gothic+One&display=swap">
<style>
  :root {
    --backdrop: #ffffff;
    --cover: #d96b45;
    --cover-dark: #c95a36;
    --corner: #f0896a;
    --brass: #efe08a;
    --sheet: #ffffff;
    --texture: #f3f3f3;
    --band: #e6eed8;
    --ink: #1c1c1c;
    --accent: #e01b1b;
  }
  * { box-sizing: border-box; margin: 0; padding: 0; }
  html, body {
    width: 1200px; height: 1095px; overflow: hidden;
    background: var(--backdrop);
  }
  body {
    font-family: "Pathway Gothic One", "Arial Narrow", sans-serif;
    color: var(--ink);
  }
  .menu-cover {
    position: absolute; left: 40px; top: 40px;
    width: 1120px; height: 1015px;
    background: var(--cover);
    display: flex; gap: 10px; padding: 0;
    box-shadow: 0 6px 18px rgba(0,0,0,.18);
  }
  .menu-cover::after {
    content: ""; position: absolute; left: 555px; top: 0;
    width: 10px; height: 100%; background: var(--cover-dark);
  }
  .page-panel {
    position: relative; width: 555px; height: 100%;
  }
  .sheet {
    position: absolute; inset: 18px;
    background: var(--sheet); overflow: hidden;
  }
  .sheet-texture {
    position: absolute; top: 0; bottom: 0; width: 70px;
    background: linear-gradient(90deg, var(--texture), #fafafa);
  }
  .sheet-texture.left { left: 0; }
  .sheet-texture.right { right: 0; background: linear-gradient(270deg, var(--texture), #fafafa); }
  .corner {
    position: absolute; width: 140px; height: 140px; background: var(--corner);
  }
  .corner.tl { top: 0; left: 0; clip-path: polygon(0 0, 100% 0, 0 100%); }
  .corner.tr { top: 0; right: 0; clip-path: polygon(0 0, 100% 0, 100% 100%); }
  .corner.bl { bottom: 0; left: 0; clip-path: polygon(0 0, 0 100%, 100% 100%); }
  .corner.br { bottom: 0; right: 0; clip-path: polygon(100% 0, 100% 100%, 0 100%); }
  .brass {
    position: absolute; width: 34px; height: 34px;
    border: 7px solid var(--brass);
  }
  .brass.tl { top: 0; left: 0; border-right: 0; border-bottom: 0; }
  .brass.tr { top: 0; right: 0; border-left: 0; border-bottom: 0; }
  .brass.bl { bottom: 0; left: 0; border-right: 0; border-top: 0; }
  .brass.br { bottom: 0; right: 0; border-left: 0; border-top: 0; }
  .page-content {
    position: relative; z-index: 1;
    text-align: center; padding-top: 70px;
  }
  .section-title {
    font-size: 36px; letter-spacing: 3px; font-weight: 400;
    margin-bottom: 40px;
  }
  .section-title .initial { color: var(--accent); }
  .menu-item { margin-bottom: 30px; }
  .item-name {
    display: block; width: 340px; margin: 0 auto 12px;
    background: var(--band);
    font-size: 21px; letter-spacing: 1.5px; font-weight: 400;
    padding: 4px 0;
  }
  .item-desc {
    font-size: 18px; letter-spacing: 1.5px; line-height: 1.1;
    width: 320px; margin: 0 auto 10px;
  }
  .item-desc .variant { text-transform: uppercase; }
  .item-price { font-size: 20px; margin-bottom: 14px; }
  .brand-sign {
    position: absolute; left: 0; right: 0; bottom: 130px; z-index: 1;
    display: flex; justify-content: center; align-items: center; gap: 12px;
    font-size: 40px; letter-spacing: 4px; color: var(--ink);
  }
  .brand-dot {
    width: 22px; height: 22px; border-radius: 50%; background: var(--ink);
  }
</style>
</head>
<body>
  <div class="menu-cover">
    <section class="page-panel">
      <div class="sheet">
        <div class="sheet-texture left" role="img" aria-label="Faint grey wave pattern strip"></div>
        <div class="sheet-texture right" role="img" aria-label="Faint grey wave pattern strip"></div>
        <div class="corner tl"></div><div class="corner tr"></div>
        <div class="corner bl"></div><div class="corner br"></div>
        <div class="page-content">
          <h2 class="section-title"><span class="initial">S</span>tarters</h2>
          <div class="menu-item">
            <h3 class="item-name">Edamame</h3>
            <p class="item-desc"><span class="variant">Steamed:</span> Soybeans, salted</p>
            <p class="item-price">5</p>
            <p class="item-desc"><span class="variant">Spicy:</span> Soybeans, sautéed with sesame oil &amp; sea salt</p>
            <p class="item-price">6</p>
          </div>
          <div class="menu-item">
            <h3 class="item-name">Shishito pepper</h3>
            <p class="item-desc">Sautéed</p>
            <p class="item-price">8</p>
          </div>
          <div class="menu-item">
            <h3 class="item-name">Agedashi Tofu</h3>
            <p class="item-desc">Fried with scallions, bonito flakes, dashi sauce</p>
            <p class="item-price">8</p>
          </div>
          <div class="menu-item">
            <h3 class="item-name">Spicy Rock Shrimp</h3>
            <p class="item-desc">Tempura battered squid tossed with shichimi pepper powder, with spicy aioli sauce</p>
            <p class="item-price">12</p>
          </div>
          <div class="menu-item">
            <h3 class="item-name">Shrimp shumai</h3>
            <p class="item-desc">Shrimp dumplings served steamed or deep fried with a seasoned soy dipping sauce</p>
            <p class="item-price">7</p>
          </div>
        </div>
      </div>
      <div class="brass tl"></div><div class="brass bl"></div>
    </section>
    <section class="page-panel">
      <div class="sheet">
        <div class="sheet-texture left" role="img" aria-label="Faint grey wave pattern strip"></div>
        <div class="sheet-texture right" role="img" aria-label="Faint grey wave pattern strip"></div>
        <div class="corner tl"></div><div class="corner tr"></div>
        <div class="corner bl"></div><div class="corner br"></div>
        <div class="page-content">
          <h2 class="section-title"><span class="initial">S</span>oup</h2>
          <div class="menu-item">
            <h3 class="item-name">Miso Soup</h3>
            <p class="item-desc"><span class="variant">Original:</span> Silken tofu and scallions in miso broth</p>
            <p class="item-price">3</p>
            <p class="item-desc"><span class="variant">Little neck clam miso:</span> Lorem ipsum dolor sit amet, consectetur adipiscing elit</p>
            <p class="item-price">X</p>
          </div>
          <div class="menu-item">
            <h3 class="item-name">Dobin Mushi pot soup</h3>
            <p class="item-desc">Lorem ipsum dolor sit amet, consectetur adipiscing elit</p>
            <p class="item-price">X</p>
          </div>
          <div class="menu-item">
            <h3 class="item-name">Kabocha Pumpkin soup</h3>
            <p class="item-desc">Creamy Asian pumpkin with a mild ginger aroma</p>
            <p class="item-price">6</p>
          </div>
        </div>
        <div class="brand-sign"><span class="brand-dot"></span><span>Mizuro</span></div>
      </div>
      <div class="brass tr"></div><div class="brass br"></div>
    </section>
  </div>
</body>
</html>
```